Bathroom Renovation Business card design needed

Bathroom, Kitchen & Laundry Renovations
Mainly complete bathroom renovations

Target Market(s)

people wanting a total bathroom renovations and other trades people

Industry/Entity Type

Business

Contact Information for Business Card

Holt Bathrooms
Dara Holt
Mobile: 0487 226504
Licence no: 604519K
Email: holtbathrooms@postlane.net

Logo styles of interest
Lettermark Logo
Requirements
Must have
• the business card should be predominantly blue
Nice to have
• the HB logo featured in the business card will be used on tshirts,tax invoices , letters etc so the HB will be the main feature, and preferably blue
Should not have
• We found the red HB logo through google images. We understand that it cannot be exactly the same but we like how the HB is linked. The example business card is something we designed but we prefer more blues. Maybe different shades of blue.

```html
<!DOCTYPE html>
<html lang="en">
<head>
<meta charset="utf-8">
<title>Holt Bathrooms – Business Card</title>
<link rel="stylesheet" href="https://fonts.googleapis.com/css2?family=Roboto:wght@300;400&family=Roboto+Condensed:wght@700&display=swap">
<style>
  :root {
    --backdrop: #0f4c76;
    --brand-blue: #52a3dc;
    --brand-blue-deep: #3f8fcd;
    --band-pale: #d3e3f4;
    --band-pale-edge: #bcd3ec;
    --paper: #ffffff;
    --ink: #444a50;
    --logo-white: #f2f4f6;
  }
  * { margin: 0; padding: 0; box-sizing: border-box; }
  html, body { width: 1200px; height: 750px; overflow: hidden; }
  body {
    background: var(--backdrop);
    font-family: "Roboto", Arial, sans-serif;
    position: relative;
  }
  .card {
    position: absolute;
    top: 220px;
    width: 540px;
    height: 309px;
    overflow: hidden;
    box-shadow: 0 10px 30px rgba(0, 0, 0, 0.35);
  }

  /* Back of card */
  .card-back { left: 45px; background: var(--brand-blue); }
  .card-back .fold {
    position: absolute; left: 0; right: 0; top: 206px; height: 60px;
    background: linear-gradient(to bottom, rgba(255,255,255,0.18), rgba(255,255,255,0) 80%);
    border-top: 1px solid rgba(255,255,255,0.35);
  }
  .card-back .base-band {
    position: absolute; left: 0; right: 0; bottom: 0; height: 44px;
    background: #6db3e3;
    border-top: 1px solid rgba(255,255,255,0.3);
  }
  .lettermark {
    position: absolute; left: 0; right: 0; top: 78px;
    text-align: center;
    font-family: "Roboto", Arial, sans-serif;
    font-weight: 400;
    font-size: 120px;
    line-height: 1;
    color: var(--logo-white);
    letter-spacing: 2px;
  }

  /* Front of card */
  .card-front { left: 615px; background: var(--paper); }
  .card-front .base-band {
    position: absolute; left: 0; right: 0; bottom: 0; height: 54px;
    background: linear-gradient(to bottom, var(--band-pale-edge), var(--band-pale));
    box-shadow: 0 -2px 6px rgba(0,0,0,0.12);
  }
  .holder-name {
    position: absolute; right: 28px; top: 26px;
    font-weight: 300; font-size: 30px; color: var(--brand-blue-deep);
  }
  .contact-panel {
    position: absolute; left: 345px; top: 78px; width: 195px; height: 150px;
    box-shadow: -6px 4px 10px -4px rgba(0,0,0,0.25);
  }
  .contact-item { position: absolute; left: 0; right: 10px; }
  .contact-item .label {
    display: block;
    font-family: "Roboto Condensed", "Arial Narrow", sans-serif;
    font-weight: 700; font-size: 15px; color: var(--brand-blue-deep);
    text-align: center;
  }
  .contact-item .value {
    display: flex; align-items: center; gap: 8px;
    font-size: 10px; color: var(--ink); margin-top: 3px; padding-left: 12px;
  }
  .contact-item svg { flex: none; }
  .item-email { top: 10px; }
  .item-mobile { top: 58px; }
  .item-licence { top: 106px; }
  .item-licence .value { font-size: 10px; }
  .item-licence .prefix { font-size: 14px; font-weight: 300; }

  .business-name {
    position: absolute; left: 66px; top: 196px;
    display: flex; align-items: center; gap: 12px;
  }
  .business-name .marker {
    width: 30px; height: 30px; background: var(--brand-blue);
  }
  .business-name .wordmark {
    font-weight: 300; font-size: 34px; color: var(--brand-blue-deep);
  }
</style>
</head>
<body>

  <section class="card card-back" aria-label="Card back">
    <div class="fold"></div>
    <div class="base-band"></div>
    <div class="lettermark">HB</div>
  </section>

  <section class="card card-front" aria-label="Card front">
    <div class="base-band"></div>
    <h1 class="holder-name">Dara Holt</h1>

    <div class="contact-panel">
      <div class="contact-item item-email">
        <span class="label">Email</span>
        <span class="value">
          <svg width="14" height="10" viewBox="0 0 14 10" aria-hidden="true">
            <rect x="0.5" y="0.5" width="13" height="9" fill="none" stroke="#666"/>
            <path d="M0.5 0.5 L7 5.5 L13.5 0.5" fill="none" stroke="#666"/>
          </svg>
          holtbathrooms@postlane.net
        </span>
      </div>
      <div class="contact-item item-mobile">
        <span class="label">Mobile</span>
        <span class="value">
          <svg width="8" height="13" viewBox="0 0 8 13" aria-hidden="true">
            <rect x="0.5" y="0.5" width="7" height="12" rx="1" fill="none" stroke="#666"/>
            <rect x="2" y="2" width="4" height="7" fill="#999"/>
          </svg>
          0487 226504
        </span>
      </div>
      <div class="contact-item item-licence">
        <span class="label">Licence</span>
        <span class="value"><span class="prefix">no:</span> 604519K</span>
      </div>
    </div>

    <div class="business-name">
      <span class="marker"></span>
      <span class="wordmark">Holt Bathrooms</span>
    </div>
  </section>

</body>
</html>
```